Marlowe Sail Works President Business Card Carbon fiber catamarans

Hi.. I need a new business card design.. I am the President of a high tech yacht builder. We build Carbon Fiber go fast catamarans... Maybe we use the file I am sharing to you as the back of the card.. We need to look cool and crisp ...

Target Market(s)

Affluent People who will purchase a cool yacht

Industry/Entity Type

Custom Yacht Builder

Contact Information for Business Card

Dean Pellington , President, 512.608.3419 USA

Font styles to use
Serif

Requirements
Must have
• the clean crisp cool feel
Nice to have
• clean and crisp
Should not have
• Bold ugly

```html
<!DOCTYPE html>
<html lang="en">
<head>
<meta charset="UTF-8">
<title>Marlowe Sail Works – Business Card</title>
<link href="https://fonts.googleapis.com/css2?family=Oswald:wght@300;500&family=Open+Sans:wght@400;600;700&display=swap" rel="stylesheet">
<style>
  :root {
    --backdrop: #3b4253;
    --navy: #0d1a2e;
    --navy-deep: #0a1526;
    --silver: #d9dde2;
    --silver-dark: #a7adb5;
    --white: #ffffff;
    --muted: #b9bec6;
  }
  * { margin: 0; padding: 0; box-sizing: border-box; }
  html, body { width: 1200px; height: 815px; overflow: hidden; }
  body {
    background: var(--backdrop);
    position: relative;
    font-family: "Open Sans", sans-serif;
  }
  .card {
    position: absolute;
    top: 253px;
    width: 540px;
    height: 309px;
  }
  /* Back of card */
  .card-back {
    left: 40px;
    background: var(--navy);
    overflow: hidden;
  }
  .texture {
    position: absolute;
    inset: 0;
    background: linear-gradient(135deg, #16243b 0%, #0d1a2e 55%, #0a1424 100%);
  }
  .back-wordmark {
    position: absolute;
    left: 46px;
    bottom: 62px;
    color: var(--silver);
    font-family: "Open Sans", sans-serif;
    font-weight: 700;
    line-height: 1.05;
    letter-spacing: 5px;
    text-transform: uppercase;
  }
  .back-wordmark .line-one { display: block; font-size: 40px; }
  .back-wordmark .line-two { display: block; font-size: 24px; letter-spacing: 6px; }

  /* Front of card */
  .card-front {
    left: 620px;
    background: linear-gradient(135deg, #f2f4f6, var(--silver) 50%, var(--silver-dark));
    padding: 11px;
  }
  .front-panel {
    position: relative;
    width: 100%;
    height: 100%;
    background: var(--navy);
  }
  .divider-bar {
    position: absolute;
    left: 246px;
    top: 0;
    width: 20px;
    height: 136px;
    background: var(--white);
  }
  .front-wordmark {
    position: absolute;
    left: 30px;
    top: 104px;
    display: flex;
    align-items: center;
    gap: 10px;
    color: var(--white);
    font-weight: 700;
    text-transform: uppercase;
    line-height: 1;
  }
  .front-wordmark .mark-square {
    width: 30px;
    height: 30px;
    background: var(--white);
  }
  .front-wordmark .line-one { display: block; font-size: 22px; letter-spacing: 3px; }
  .front-wordmark .line-two { display: block; font-size: 13px; letter-spacing: 3.5px; margin-top: 2px; }
  .person {
    position: absolute;
    left: 272px;
    top: 112px;
  }
  .person-name {
    font-family: "Oswald", sans-serif;
    font-weight: 300;
    font-size: 29px;
    color: var(--white);
    text-transform: uppercase;
    letter-spacing: 0.5px;
    line-height: 1;
  }
  .person-name strong { font-weight: 500; }
  .person-title {
    margin-top: 5px;
    font-size: 11px;
    font-weight: 700;
    letter-spacing: 1px;
    color: var(--muted);
  }
  .contacts {
    position: absolute;
    left: 252px;
    top: 186px;
    list-style: none;
  }
  .contacts li {
    display: flex;
    align-items: center;
    gap: 12px;
    height: 22px;
    margin-bottom: 13px;
    font-size: 11px;
    color: var(--white);
    letter-spacing: 0.3px;
  }
  .contact-icon {
    width: 22px;
    height: 22px;
    background: var(--white);
    border-radius: 0 11px 11px 0;
    display: flex;
    align-items: center;
    justify-content: center;
    flex-shrink: 0;
  }
  .contact-icon svg { width: 13px; height: 13px; fill: var(--navy); }
</style>
</head>
<body>

  <section class="card card-back" aria-label="Back of business card">
    <div class="texture" role="img" aria-label="Dark navy carbon fibre texture"></div>
    <div class="back-wordmark">
      <span class="line-one">Marlowe</span>
      <span class="line-two">Sail Works</span>
    </div>
  </section>

  <section class="card card-front" aria-label="Front of business card">
    <div class="front-panel">
      <div class="divider-bar"></div>

      <div class="front-wordmark">
        <span class="mark-square"></span>
        <div>
          <span class="line-one">Marlowe</span>
          <span class="line-two">Sail Works</span>
        </div>
      </div>

      <div class="person">
        <h1 class="person-name"><strong>Dean</strong> Pellington</h1>
        <p class="person-title">PRESIDENT</p>
      </div>

      <ul class="contacts">
        <li>
          <span class="contact-icon">
            <svg viewBox="0 0 24 24"><path d="M6.6 10.8a15.1 15.1 0 0 0 6.6 6.6l2.2-2.2c.3-.3.7-.4 1-.2 1.1.4 2.3.6 3.6.6.6 0 1 .4 1 1V20c0 .6-.4 1-1 1A17 17 0 0 1 3 4c0-.6.4-1 1-1h3.5c.6 0 1 .4 1 1 0 1.3.2 2.5.6 3.6.1.3 0 .7-.2 1z"/></svg>
          </span>
          512.608.3419
        </li>
        <li>
          <span class="contact-icon">
            <svg viewBox="0 0 24 24"><path d="M5 2l14 11-6.2.8 3.7 7.4-2.6 1.3-3.7-7.4L5 19.5z"/></svg>
          </span>
          www.marlowesailworks.com
        </li>
        <li>
          <span class="contact-icon">
            <svg viewBox="0 0 24 24"><path d="M12 2a7 7 0 0 0-7 7c0 5.2 7 13 7 13s7-7.8 7-13a7 7 0 0 0-7-7zm0 9.5A2.5 2.5 0 1 1 12 6.5a2.5 2.5 0 0 1 0 5z"/></svg>
          </span>
          P.O. Box 218, Lakeway, TX 78734
        </li>
      </ul>
    </div>
  </section>

</body>
</html>
```